Job Coaching - Mova; engaging people to improve their work experience

design a website focussed on people
with 4 tabs/pages (+2)
1) landing page
2) Professional
3) Job Coaching
4) Bio
5) Contact
6) references

I've added the text to be used in the documents. The website will be in Dutch, but I've added the translations in green just for you to understand what it is about.

I've added my logo as well, and a flyer I used already. this gives you an idea on how it could look like
Pictures you can find there as well. Other pictures can be added of course
The techical creation of the website is not needed. I need all the designs and information to be able to create it myself.

```html
<!DOCTYPE html>
<html lang="nl">
<head>
<meta charset="utf-8">
<title>Mova – professionele begeleiding</title>
<link href="https://fonts.googleapis.com/css2?family=Rubik:wght@400;500;600&family=Inter:wght@300;400;500;600&display=swap" rel="stylesheet">
<style>
  :root{
    --canvas:#e8e8e8;
    --teal:#3aa99c;
    --ink:#222222;
    --text:#555555;
    --white:#ffffff;
    --footer-dark:#1e1e1e;
    --footer-light:#3d3d3d;
    --rule:#8a8a8a;
  }
  *{margin:0;padding:0;box-sizing:border-box}
  html,body{width:1200px;height:948px;overflow:hidden}
  body{background:var(--canvas);font-family:"Inter",sans-serif;color:var(--ink);position:relative}

  .page{position:absolute;top:42px;width:528px;overflow:hidden;background:var(--white)}
  .page--curved{left:52px;height:863px;background:linear-gradient(135deg,var(--footer-dark),var(--footer-light))}
  .page--straight{left:620px;height:832px}

  /* header */
  .site-header{position:absolute;left:0;top:0;width:100%;height:30px;background:var(--white);z-index:3}
  .page--straight .site-header{height:32px}
  .brand{position:absolute;left:45px;top:7px;display:flex;align-items:center;gap:5px;font-family:"Rubik",sans-serif;font-weight:500;font-size:17px;line-height:1;color:var(--teal)}
  .brand__dot{width:16px;height:16px;border-radius:50%;background:var(--teal)}
  .main-nav{position:absolute;left:240px;top:0;height:100%;display:flex;font-family:"Rubik",sans-serif;font-weight:500;font-size:6.6px;color:var(--ink)}
  .main-nav a{color:inherit;text-decoration:none;display:flex;align-items:center;padding:0 6px;height:100%}
  .main-nav a.is-active{background:var(--teal);color:var(--white);width:31px;justify-content:center;padding:0}
  .page--curved .main-nav a.is-active{height:44px;align-items:flex-start;padding-top:12px;border-radius:0 0 15px 15px}

  /* hero */
  .hero-visual{position:absolute;left:0;width:100%}
  .page--curved .hero-visual{top:30px;height:400px;background:linear-gradient(110deg,#2d3236 0%,#5a5e60 45%,#9fb6cc 75%,#4e5e70 100%)}
  .page--straight .hero-visual{top:32px;height:302px;background:linear-gradient(120deg,#3fb7d6 0%,#1c95bd 55%,#17607a 100%)}
  .hero-shape{position:absolute;left:0;top:0;z-index:1}

  .hero-copy{position:absolute;z-index:2;color:var(--white)}
  .hero-title{font-family:"Rubik",sans-serif;font-weight:500;font-size:38px;line-height:1;letter-spacing:.5px}
  .hero-subtitle{font-family:"Rubik",sans-serif;font-weight:500;font-size:13.5px;margin-top:4px}
  .hero-button{display:inline-flex;align-items:center;justify-content:center;font-family:"Rubik",sans-serif;font-weight:600;font-size:6px;color:var(--white);border-radius:11px}
  .page--curved .hero-copy{left:64px;top:130px}
  .page--curved .hero-title{color:var(--teal)}
  .page--curved .hero-button{margin-top:6px;width:64px;height:19px;background:var(--teal)}
  .hero-bar{position:absolute;left:52px;top:134px;width:3px;height:75px;background:var(--teal);z-index:2}
  .page--straight .hero-copy{left:0;width:100%;top:130px;text-align:center}
  .page--straight .hero-button{margin-top:8px;width:66px;height:21px;border:1.5px solid var(--white)}

  .slider-dots{position:absolute;left:251px;display:flex;gap:3px;z-index:2}
  .page--curved .slider-dots{top:270px}
  .page--straight .slider-dots{top:301px}
  .slider-dots span{width:6px;height:6px;border:1px solid var(--white);border-radius:50%}
  .slider-dots span.is-current{width:7px;height:7px;margin-top:-.5px;background:radial-gradient(circle,var(--white) 0 1.5px,transparent 1.6px)}

  /* intro */
  .coach-portrait{position:absolute;left:63px;top:381px;width:176px;height:176px;border-radius:50%;background:radial-gradient(circle at 45% 40%,#8c2a34 0 30%,#3aa99c 31% 55%,#636363 56%);z-index:2}
  .intro{position:absolute;left:271px;top:359px;width:208px;z-index:2}
  .intro__hello{font-family:"Rubik",sans-serif;font-weight:500;font-size:9.5px;color:var(--ink)}
  .intro__name{font-family:"Rubik",sans-serif;font-weight:500;font-size:19px;color:var(--teal);margin-top:4px;line-height:1.1}
  .intro__text{font-weight:300;font-size:5.9px;line-height:11.3px;color:var(--text);text-align:justify;margin-top:6px}
  .intro__text + .intro__text{margin-top:11.3px}
  .call-to-action{position:absolute;left:64px;top:585px;width:400px;text-align:center;font-family:"Rubik",sans-serif;font-weight:500;font-size:9.6px;line-height:15px;color:var(--ink);z-index:2}

  /* footer */
  .page--straight .footer-band{position:absolute;left:0;top:652px;width:100%;height:180px;background:linear-gradient(135deg,var(--footer-dark),var(--footer-light))}
  .site-footer{position:absolute;left:0;width:100%;color:var(--white);z-index:2}
  .page--curved .site-footer{top:717px}
  .page--straight .site-footer{top:691px}
  .footer-col{position:absolute;top:0}
  .footer-col:nth-child(1){left:48px;width:118px}
  .footer-col:nth-child(2){left:196px}
  .footer-col:nth-child(3){left:317px}
  .footer-col:nth-child(4){left:417px}
  .footer-col h3{font-family:"Rubik",sans-serif;font-weight:500;font-size:9.5px;line-height:12px}
  .footer-rule{position:absolute;top:21px;left:0;width:62px;height:1px;background:var(--rule)}
  .footer-rule::before{content:"";position:absolute;left:1px;top:-2px;width:4px;height:4px;background:var(--teal);transform:rotate(45deg)}
  .footer-col p,.footer-col ul{position:absolute;top:36px;left:0;font-size:6.1px;line-height:9.4px;list-style:none;white-space:nowrap}
  .footer-col p{white-space:normal;width:118px}
  .social-list{position:absolute;top:37px;left:1px;list-style:none}
  .social-list li{display:flex;align-items:center;gap:5px;height:19px;font-size:6.1px}
  .social-list li::before{content:"";width:15px;height:15px;border-radius:50%;background:var(--white)}
  .copyright{position:absolute;left:0;width:100%;text-align:center;font-size:6.4px;color:var(--white);z-index:2}
  .page--curved .copyright{top:834px}
  .page--straight .copyright{top:812px}
</style>
</head>
<body>

<section class="page page--curved">
  <header class="site-header">
    <div class="brand"><span class="brand__dot"></span>Mova</div>
    <nav class="main-nav">
      <a class="is-active">Home</a><a>Professioneel</a><a>Jobcoaching</a><a>Bio</a><a>Contact</a><a>Referenties</a>
    </nav>
  </header>
  <div class="hero-visual" role="img" aria-label="Foto van twee zakenmannen die elkaar glimlachend de hand schudden op kantoor"></div>
  <svg class="hero-shape" width="528" height="863" viewBox="0 0 528 863">
    <path d="M0,388 Q264,222 528,388 L528,602 Q264,762 0,602 Z" fill="#ffffff"/>
    <path d="M73,358 Q290,272 453,345" fill="none" stroke="#3aa99c" stroke-width="4" stroke-linecap="round"/>
    <path d="M73,647 Q264,719 457,630" fill="none" stroke="#3aa99c" stroke-width="4" stroke-linecap="round"/>
  </svg>
  <span class="hero-bar"></span>
  <div class="hero-copy">
    <h1 class="hero-title">MOVA</h1>
    <p class="hero-subtitle">Professionele begeleiding</p>
    <a class="hero-button">BEGIN</a>
  </div>
  <div class="slider-dots"><span></span><span class="is-current"></span><span></span><span></span></div>

  <div class="coach-portrait" role="img" aria-label="Portretfoto van de coach in rood hemd voor een kompasvormig teal en grijs embleem"></div>
  <article class="intro">
    <p class="intro__hello">Hallo,</p>
    <h2 class="intro__name">ik ben Bram Peeters</h2>
    <p class="intro__text">Als gepassioneerd loopbaancoach wil ik jou in je kracht zetten bij het uitoefenen van je job, elke dag opnieuw. We blijven steeds langer aan de slag en daarom is het vandaag meer dan ooit belangrijk om de nodige aandacht te besteden aan professionele groei en welzijn op het werk. Ik ben ervan overtuigd dat mensen vaak tot meer in staat zijn dan ze zelf geloven. Alles begint met het verlangen naar verandering. Wie ben ik? Wat is mijn rol? Wat wil ik écht?</p>
    <p class="intro__text">Als jobcoach ga ik niet voor eenvoudige quick-wins of kant-en-klare tips en tricks. In een geest van openheid, vertrouwen en gelijkwaardigheid gaan we samen op zoek naar de diepere inzichten en duurzame oplossingen die voor jou werken. Coaching is een bewustwordingsproces dat leidt tot het vinden van de antwoorden in jezelf.</p>
  </article>
  <p class="call-to-action">Meld je vandaag nog aan voor een vrijblijvend kennismakingsgesprek en neem de regie van je loopbaan (opnieuw) in handen.</p>

  <footer class="site-footer">
    <div class="footer-col"><h3>Professioneel</h3><span class="footer-rule"></span><p>Mijn job als arbeidspsycholoog en mijn jarenlange ervaring in de HR-sector hebben me geleerd hoe belangrijk het is dat medewerkers en managers in hun staan in de functie die ze uitoefenen.</p></div>
    <div class="footer-col"><h3>Meer te weten komen</h3><span class="footer-rule"></span><ul><li>Over ons</li><li>Ons team</li><li>Onze klanten</li><li>Contact</li><li>Carrières</li></ul></div>
    <div class="footer-col"><h3>Snelle links</h3><span class="footer-rule"></span><ul><li>Thuis</li><li>Over</li><li>Carrière</li><li>bloggen</li><li>Contact</li></ul></div>
    <div class="footer-col"><h3>Volg ons</h3><span class="footer-rule"></span><ul class="social-list"><li>Nieuwsbrief</li><li>Netwerk</li><li>Fotoblog</li></ul></div>
  </footer>
  <p class="copyright">© 2023 Mova.Alle rechten voorbehouden | Privacybeleid | Voorwaarden</p>
</section>

<section class="page page--straight">
  <header class="site-header">
    <div class="brand"><span class="brand__dot"></span>Mova</div>
    <nav class="main-nav">
      <a class="is-active">Home</a><a>Professioneel</a><a>Jobcoaching</a><a>Bio</a><a>Contact</a><a>Referenties</a>
    </nav>
  </header>
  <div class="hero-visual" role="img" aria-label="Foto van een houten figuurtje dat een trap van houten blokjes oploopt, een hand plaatst de volgende trede, op blauwe achtergrond"></div>
  <div class="hero-copy">
    <h1 class="hero-title">MOVA</h1>
    <p class="hero-subtitle">Professionele begeleiding</p>
    <a class="hero-button">BEGIN</a>
  </div>
  <div class="slider-dots"><span></span><span class="is-current"></span><span></span><span></span></div>

  <div class="coach-portrait" role="img" aria-label="Portretfoto van de coach in rood hemd voor een kompasvormig teal en grijs embleem"></div>
  <article class="intro">
    <p class="intro__hello">Hallo,</p>
    <h2 class="intro__name">ik ben Bram Peeters</h2>
    <p class="intro__text">Als gepassioneerd loopbaancoach wil ik jou in je kracht zetten bij het uitoefenen van je job, elke dag opnieuw. We blijven steeds langer aan de slag en daarom is het vandaag meer dan ooit belangrijk om de nodige aandacht te besteden aan professionele groei en welzijn op het werk. Ik ben ervan overtuigd dat mensen vaak tot meer in staat zijn dan ze zelf geloven. Alles begint met het verlangen naar verandering. Wie ben ik? Wat is mijn rol? Wat wil ik écht?</p>
    <p class="intro__text">Als jobcoach ga ik niet voor eenvoudige quick-wins of kant-en-klare tips en tricks. In een geest van openheid, vertrouwen en gelijkwaardigheid gaan we samen op zoek naar de diepere inzichten en duurzame oplossingen die voor jou werken. Coaching is een bewustwordingsproces dat leidt tot het vinden van de antwoorden in jezelf.</p>
  </article>
  <p class="call-to-action">Meld je vandaag nog aan voor een vrijblijvend kennismakingsgesprek en neem de regie van je loopbaan (opnieuw) in handen.</p>

  <div class="footer-band"></div>
  <footer class="site-footer">
    <div class="footer-col"><h3>Professioneel</h3><span class="footer-rule"></span><p>Mijn job als arbeidspsycholoog en mijn jarenlange ervaring in de HR-sector hebben me geleerd hoe belangrijk het is dat medewerkers en managers in hun staan in de functie die ze uitoefenen.</p></div>
    <div class="footer-col"><h3>Meer te weten komen</h3><span class="footer-rule"></span><ul><li>Over ons</li><li>Ons team</li><li>Onze klanten</li><li>Contact</li><li>Carrières</li></ul></div>
    <div class="footer-col"><h3>Snelle links</h3><span class="footer-rule"></span><ul><li>Thuis</li><li>Over</li><li>Carrière</li><li>bloggen</li><li>Contact</li></ul></div>
    <div class="footer-col"><h3>Volg ons</h3><span class="footer-rule"></span><ul class="social-list"><li>Nieuwsbrief</li><li>Netwerk</li><li>Fotoblog</li></ul></div>
  </footer>
  <p class="copyright">© 2023 Mova.Alle rechten voorbehouden | Privacybeleid | Voorwaarden</p>
</section>

</body>
</html>
```